Luxury Face Oil Label

I'm looking for a simple and sophisticated design for a natural face oil that will target the luxe market. It is a pure Natural product. I have attached the logo, Velumi Organics.

Here's the Copy

LUXE FACIAL OIL

Regenerate. Hydrate. Glow

100% Natural

30ml (1.01 oz)

A complex blend of Pure Oils including Marula, Sea Buckthorn, Rosehip, Neroli, Evening primrose, Argan, Calendula, Lavender, Jojoba, Grapeseed, Baobab, Moringa and Vitamin E oil.

Produced by
Brasso Kettle Ltd
P.O box 7925-00300
Nairobi, Kenya
www.velumiorganics.example

Target Market(s)

High end

Requirements
Must have
• Simple, Please consider the bottle, which is a 30ml clear glass bottle with a gold and white pump. Image attached.
Nice to have
• Very clean designs, not too much going on.
Should not have
• Leaves and nuts.

```html
<!DOCTYPE html>
<html lang="en">
<head>
<meta charset="utf-8">
<title>Luxe Facial Oil Label</title>
<link href="https://fonts.googleapis.com/css2?family=Didact+Gothic&display=swap" rel="stylesheet">
<style>
:root{
  --ink:#3f5232;
  --sage:#b3c98f;
  --sage-soft:#dfe9cf;
  --paper:#ffffff;
}
*{margin:0;padding:0;box-sizing:border-box}
html,body{width:1200px;height:1200px;overflow:hidden;background:var(--paper)}
body{font-family:"Didact Gothic","Century Gothic",sans-serif;color:var(--ink)}
.label{position:relative;width:1200px;height:1200px}
.label-frame{position:absolute;left:80px;top:78px;width:1081px;height:1081px;border:3px solid var(--sage)}
.product-title{position:absolute;left:0;width:1231px;top:128px;text-align:center;font-size:86px;letter-spacing:9px;font-weight:400;line-height:1.1}
.title-rule{position:absolute;left:224px;top:261px;width:786px;height:4px;background:var(--sage)}
.tagline{position:absolute;left:0;width:1231px;top:305px;text-align:center;font-size:33px;line-height:51px}
.botanical-art{position:absolute;left:318px;top:432px;width:600px;height:312px;
  background:radial-gradient(ellipse at 55% 55%,var(--sage-soft) 0%,rgba(223,233,207,0.5) 45%,rgba(255,255,255,0) 72%)}
.ingredients{position:absolute;left:173px;top:782px;width:420px;font-size:31px;line-height:37.5px}
.producer{position:absolute;left:728px;top:782px;width:340px;font-size:31px;line-height:37.5px}
.volume{position:absolute;right:62px;top:1094px;font-size:25px;letter-spacing:0.5px}
</style>
</head>
<body>
<main class="label">
  <div class="label-frame"></div>
  <h1 class="product-title">LUXE FACIAL OIL</h1>
  <div class="title-rule"></div>
  <p class="tagline">Regenerate. Hydrate. Glow<br>100% Natural</p>
  <div class="botanical-art" role="img" aria-label="Line illustration of a slender leafy branch in pale sage green"></div>
  <p class="ingredients">A complex blend of Pure Oils including Marula, Sea Buckthorn, Rosehip, Neroli, Evening primrose, Argan, Calendula, Lavender, Jojoba, Grapeseed, Baobab, Moringa and Vitamin E oil.</p>
  <p class="producer">Produced by<br>Brasso Kettle Ltd<br>P.O box 7925-00300<br>Nairobi, Kenya<br>www.velumiorganics.<br>example</p>
  <p class="volume">30ml (1.01 oz)</p>
</main>
</body>
</html>
```